We need a template newsletter design for our quarterly newsletter that we issue to employees. The newsletter generally holds updates from different departments such as:

CEO
Finance
Operations
Human Resources, ETC
(Please allow the pages to be copied)

I am looking for a template that has headings on each page, text space and image space. I am looking for a funky hip design with some great colour and creative imagination.

If you could create a cover page that includes the name "Harbourlinks" and the edition "Month, Year".

There is no requirements for specific logos or colours to be incorporated into this newsletter.

If possible I would like each page to have a different layout/design but for it to still flow as one newsletter. (Work with 4 pages/headings as listed above)

The document must be produced in InDesign.

Reason: Hi Guys, Whilst I love the designs submitted I am looking for a less formal and more creative funky design. Project is extended another 2 days. Thank you Merv

```html
<!DOCTYPE html>
<html lang="en">
<head>
<meta charset="utf-8">
<title>Harbourlinks Quarterly Newsletter – Design Idea 01a</title>
<link href="https://fonts.googleapis.com/css2?family=Montserrat:wght@700;900&family=Roboto+Condensed:wght@700&family=Open+Sans:wght@400;700&display=swap" rel="stylesheet">
<style>
:root{
  --orange:#f18b1d;
  --orange-deep:#e27a10;
  --board:#2d2d2f;
  --ink:#1f1f1f;
  --body:#555;
  --paper:#ffffff;
  --label:#c9c9c9;
  --title:#5e6873;
}
*{margin:0;padding:0;box-sizing:border-box}
html,body{width:1200px;height:1200px;overflow:hidden;background:var(--board)}
.board{position:relative;width:1200px;height:1200px;font-family:"Open Sans",sans-serif}
.board-title{position:absolute;left:72px;top:46px;font-family:"Montserrat",sans-serif;font-weight:700;font-size:31px;color:var(--title);letter-spacing:-.5px}

/* cover */
.cover{position:absolute;left:52px;top:184px;width:440px;height:688px;background:var(--orange);overflow:hidden}
.cover-head{height:130px;position:relative;color:#fff}
.cover-date,.cover-issue{position:absolute;top:8px;font-family:"Roboto Condensed",sans-serif;font-weight:700;font-size:11px}
.cover-date{left:30px}.cover-issue{right:50px}
.cover-name{position:absolute;left:0;right:0;top:28px;text-align:center;font-family:"Montserrat",sans-serif;font-weight:900;font-size:50px;letter-spacing:-1.5px}
.cover-sub{position:absolute;left:0;right:0;top:98px;text-align:center;font-size:9px;letter-spacing:-.2px}
.cover-photo{position:absolute;left:0;top:130px;width:440px;height:518px;background:linear-gradient(135deg,#10324a 0%,#2a6c8c 45%,#1b3b55 70%,#0d2033 100%)}
.cover-band{position:absolute;left:0;bottom:0;width:100%;height:40px;display:flex;align-items:center;justify-content:center;color:#fff;font-family:"Roboto Condensed",sans-serif;font-weight:700;font-size:19px;letter-spacing:-.3px}

/* spreads */
.spread{position:absolute;left:552px;width:620px;display:flex;box-shadow:0 4px 14px rgba(0,0,0,.5)}
.spread-top{top:84px;height:524px}
.spread-bottom{top:644px;height:516px}
.page{position:relative;width:310px;height:100%;background:var(--paper);overflow:hidden}
.page-left{border-right:1px solid #ddd}
.tag{position:absolute;left:12px;top:26px;width:124px;height:20px;background:var(--orange);color:#fff;font-family:"Roboto Condensed",sans-serif;font-weight:700;font-size:9px;padding:4px 5px}
.tag-over{top:18px;left:16px;width:120px;font-size:10px}
.page-foot{position:absolute;left:12px;right:6px;bottom:6px;height:18px;background:var(--orange);color:#fff;font-size:5.5px;display:flex;align-items:center;justify-content:flex-end;padding-right:24px}
.page-foot b{margin-left:3px}
.page-num{position:absolute;right:6px;top:2px;width:13px;height:14px;background:#111;color:#fff;font-weight:700;font-size:7px;display:flex;align-items:center;justify-content:center}
.photo{position:absolute}
.headline{position:absolute;font-family:"Roboto Condensed",sans-serif;font-weight:700;color:var(--ink);line-height:1.05;letter-spacing:-.3px}
.deck{position:absolute;font-size:5.6px;font-weight:700;color:var(--ink);line-height:1.45}
.col{position:absolute;overflow:hidden;font-size:4.6px;line-height:7.5px;color:var(--body);text-align:justify}
.col p{margin-bottom:6px}
.rule{position:absolute;height:2px;background:var(--orange)}
.callout{background:var(--orange);color:#fff;font-weight:700;padding:6px 4px;height:100%;text-align:left}
.callout p{margin-bottom:7px}

/* labels */
.spec{position:absolute;left:16px;font-size:17px;color:var(--label)}
.spec span{position:absolute;white-space:nowrap}
</style>
</head>
<body>
<div class="board">
  <h1 class="board-title">MAGAZINE DESIGN IDEA - 01a</h1>

  <section class="cover">
    <div class="cover-head">
      <span class="cover-date">Aug 2016</span>
      <span class="cover-issue">Issue No # 001</span>
      <div class="cover-name">HARBOURLINKS</div>
      <div class="cover-sub">Bluewater Pacific Quarterly News Letter</div>
    </div>
    <div class="cover-photo" role="img" aria-label="Hand in a business suit drawing an organisation chart of staff icons on a blue screen"></div>
    <div class="cover-band">Creating Better Customer Relationships</div>
  </section>

  <div class="spread spread-top">
    <article class="page page-left">
      <div class="tag">CEO</div>
      <h2 class="headline" style="left:12px;top:62px;font-size:19px;width:290px">CEO Speaks of Expanding in U.S., Acquiring More Companies</h2>
      <div class="col" style="left:12px;top:112px;width:142px;height:126px">
        <p>Northvale Foods Chief Executive Adrian Kessel on Thursday indicated the company isn't averse to making multibillion-dollar acquisitions should the right opportunity arise, a day after the consumer-goods giant said it was buying startup Keen Blade Club.</p>
        <p>Meeting with journalists in London following the announcement of first-half results, Mr. Kessel said the company's strategy has been to make roughly €2 billion in acquisitions a year, with the bulk of growth coming organically through investments in existing brands.</p>
      </div>
      <div class="photo" style="left:160px;top:112px;width:130px;height:120px;background:linear-gradient(160deg,#d9dde2,#8c99a6 60%,#2f3640)" role="img" aria-label="Portrait of the chief executive in a dark suit"></div>
      <div class="col" style="left:12px;top:242px;width:286px;height:252px">
        <p>Northvale has agreed to pay $1 billion in cash for Keen Blade Club, according to people familiar with that deal. The company last spring bought four high-end skin-care brands and in October bought an Italian ice cream maker.</p>
        <p>Sitting at a table strewn with brands Northvale had acquired in recent years, Mr. Kessel said the company would look at bigger deals along the lines of its earlier acquisitions if it makes sense. He declined to comment on specific categories in which the company might seek acquisitions.</p>
        <p>Northvale's first priority once it buys Keen Blade Club will be to accelerate its growth in the U.S., he said, after which the company will work to implement lessons it gets from that business's direct-to-consumer model across other units such as its tea brand and beauty brands.</p>
        <p>"We are actually buying one of the disruptors," he said. "We will learn from that. We will disrupt ourselves."</p>
        <p>Mr. Kessel blamed the U.S. elections, Britain's vote to leave the European Union, and several regional events for creating sluggish demand in a string of markets.</p>
        <p>A coup attempt abroad hurt Northvale's ice cream sales, Mr. Kessel said, adding that declines in tourism could lead to the company having to close its ice cream factories there for a couple of days.</p>
        <p>He said Northvale would look to adjust prices in Britain to compensate for the fall in the pound following the vote, but declined to specify when and by how much. The company has 10 factories in the U.K., many of which make products that are exported to Europe, he added.</p>
        <p>Despite the geographic disruptions and continued difficulties in businesses such as tea and spreads, Mr. Kessel said Northvale's diverse product and geographic mix positions it to ride out volatility. "I've always said, don't worry about Northvale," he said. "People who buy into Northvale buy into the total company."</p>
      </div>
      <footer class="page-foot">August, 2016 | <b>Quarterly News Letter</b><span class="page-num">2</span></footer>
    </article>

    <article class="page">
      <div class="photo" style="left:16px;top:18px;width:278px;height:170px;background:linear-gradient(135deg,#e8f3f7,#8fc1d6 40%,#3a7fa3 75%,#1f5478)" role="img" aria-label="Rising financial index chart with arrows over a blue grid"></div>
      <div class="tag tag-over">Finance</div>
      <div class="rule" style="left:16px;top:194px;width:278px"></div>
      <h2 class="headline" style="left:16px;top:208px;font-size:21px;width:290px">Green Finance 2016 G20 Summit</h2>
      <div class="deck" style="left:16px;top:236px;width:280px">Chinese finance officials to spearhead discussions on achieving balance among environmental protection, investment and financing through 'Green Finance' in Hangzhou's summit next month.</div>
      <div class="col" style="left:16px;top:268px;width:136px;height:226px">
        <p>Significant changes are taking place in the region's relations with countries near and far. In the immediate neighborhood, Cyprus and Greece, both members of the European Union, have established close economic and political relations. And now Turkey, a major Middle East player, will be normalizing relations as well. That, no doubt, is a prelude to closer economic and political relations based on common interests in the area, notwithstanding the differences that exist between Turkey and Cyprus and Greece, and Turkey's position on the wider regional issue.</p>
        <p>A political and economic bloc is taking shape, which may include military cooperation as well in due time that will profoundly influence the course of events in the Middle East in the years to come. No less significant are the relations that have developed with Egypt and Jordan. The regional rift and the rise of new threats have made it clear that these countries share common enemies, enemies that threaten the stability of their regimes and make security cooperation a common interest of all.</p>
      </div>
      <div class="col" style="left:158px;top:268px;width:136px;height:226px">
        <p>The rulers of Jordan and Egypt continue to pay lip-service to the regional cause, but it is clear what their immediate priorities are. And there is Saudi Arabia, the wealthiest Arab country, threatened by extremists and Iran. For obvious reasons its rulers are not prepared to establish formal relations, but here too common enemies are bound to result in developing behind-the-scenes relationships. Relations with Russia are excellent.</p>
        <p>These old and new friends see the country as a strong country militarily and economically, and therefore a country that wields significant influence in the immediate area and even beyond. It is a friend worth having. Simultaneously, it has been pivoting to the East. India, which now outranks France economically, has one of the fastest growing economies. With Pakistan as a neighbor and a large minority among its population, its problems are not dissimilar from the problems facing the country, and that leaves room for extensive cooperation that would be of mutual benefit.</p>
        <p>China, the world's second superpower, is too large to be ignored, while the country, small as it is, nevertheless</p>
      </div>
      <footer class="page-foot">August, 2016 | <b>Quarterly News Letter</b><span class="page-num">3</span></footer>
    </article>
  </div>

  <div class="spread spread-bottom">
    <article class="page page-left">
      <div class="photo" style="left:14px;top:30px;width:138px;height:128px;background:linear-gradient(135deg,#f3e2c2,#d9a766 45%,#9c6a35 75%,#e8e1d6)" role="img" aria-label="Stacked coins and a pen on a financial printout"></div>
      <div class="col" style="left:14px;top:162px;width:138px;height:34px">
        <p>is seen by China as a technological superpower. In these countries, unlike Europe, anti-Semitism is almost non-existent.</p>
      </div>
      <div class="col" style="left:14px;top:200px;width:138px;height:300px">
        <p>Prognostications regarding a deterioration of relations with the United States, its most important ally and friend, are way off the mark. It is true that the U.S. is changing, as is most of the rest of the world, and the most recent waves of immigration have changed the demographics of the country. But those who assume that this is bound to lead to a cooling of the relations between the two nations fail to understand the nature of America, a country of immigrants. The ideals and values of America are the ideals and values of America at its foundation, and they have not changed since 1776.</p>
        <p>Successive waves of immigrants have adopted these values, and that no doubt will be true with the most recent wave of immigration. It is these ideals and values, democracy and the rule of law, that are the foundation of the alliance between the two nations, and that alliance will persist despite inevitable differences of opinion that occur now and then. And there is the common cause, the battle against radical terrorism, which bonds both countries together and all the countries threatened by it.</p>
        <p>A nation which has had to contend with acts of terror for many years has by necessity become the world's expert in dealing with terrorism and its cooperation and capabilities are being sought by all those who feel threatened by it. That cooperation will serve as an important element in its relations with the world. It will not find itself isolated.</p>
      </div>
      <div class="col" style="left:160px;top:30px;width:138px;height:226px">
        <p>A political and economic bloc is taking shape, which may include military cooperation as well in due time that will profoundly influence the course of events in the Middle East in the years to come. No less significant are the relations that have developed with Egypt and Jordan. The regional rift and the rise of new threats have made it clear that these countries share common enemies, enemies that threaten the stability of the Egyptian and Jordanian regimes and make security cooperation a common interest of all.</p>
        <p>These old and new friends see the country as a strong country militarily and economically, and therefore a country that wields significant influence in the immediate area and even beyond. It is a friend worth having. Simultaneously, it has been pivoting to the East. India, which now outranks France economically, has one of the fastest growing economies. With Pakistan as a neighbor</p>
      </div>
      <div class="photo" style="left:160px;top:262px;width:138px;height:126px;background:linear-gradient(135deg,#163a54,#2f7396 50%,#112b40)" role="img" aria-label="Hand drawing an organisation chart of staff icons"></div>
      <div class="col" style="left:160px;top:392px;width:138px;height:100px">
        <p>and a large minority among its population, its problems are not dissimilar from the problems facing the country, and that leaves room for extensive cooperation that would be of mutual benefit.</p>
        <p>China, the world's second superpower, is too large to be ignored, while the country, small as it is, nevertheless is seen by China as a technological superpower. In these countries, unlike Europe, prejudice is almost non-existent.</p>
      </div>
      <footer class="page-foot">August, 2016 | <b>Quarterly News Letter</b><span class="page-num">4</span></footer>
    </article>

    <article class="page">
      <div class="photo" style="left:16px;top:18px;width:278px;height:160px;background:linear-gradient(180deg,#1c3f78 0%,#3e6fb0 45%,#8a8f96 70%,#3b3d42 100%)" role="img" aria-label="Oil refinery with storage tanks under a blue sky"></div>
      <div class="tag tag-over">Operations</div>
      <div class="rule" style="left:16px;top:184px;width:278px"></div>
      <h2 class="headline" style="left:16px;top:194px;font-size:21px;width:290px">Big Oil Finding Money for Biggest Projects</h2>
      <div class="deck" style="left:16px;top:242px;width:280px">$36.8 billion project agreed by Ridgeway Energy, Coastline Petroleum and their partners suggests oil's deep freeze might be thawing</div>
      <div class="col" style="left:16px;top:270px;width:88px;height:222px">
        <div class="callout">
          <p>There are signs the deep freeze in oil-industry spending is beginning to thaw.</p>
          <p>Ridgeway Energy, Coastline Petroleum and several partners on Tuesday committed $27 billion to expand an oil project in Kazakhstan known as Tengiz, one of the biggest investments since crude prices collapsed two years ago.</p>
          <p>Last week, Meridian Oil gave the green light to a multibillion-dollar gas export expansion complex. It follows the U.K. oil giant's announcement in June that it is fast-tracking a major offshore gas discovery, and another producer is moving ahead on an Egypt field as well.</p>
        </div>
      </div>
      <div class="col" style="left:110px;top:270px;width:88px;height:222px">
        <p>In choosing to invest now, the world's biggest energy companies get to benefit from a huge drop in drilling costs that has accompanied the oil-price fall. Pumps, valves, drilling rigs, construction and engineering services, steel and even labor are cheaper because the contractors that provided those services have less work than in the boom years after the financial crisis when oil prices traded around $100 a barrel.</p>
        <p>The recent wave of investments may point to confidence in an oil-price recovery, after they collapsed from around $115 a barrel in mid-2014 to a low of $27 in January, but it is still early days.</p>
        <p>Big-energy company executives have said they are treating the oil-price rally with caution, warning that</p>
      </div>
      <div class="col" style="left:204px;top:270px;width:90px;height:222px">
        <p>as prices rise, investment could kick in from U.S. shale producers and American output could quickly ramp up again. Just on Tuesday, U.S. crude prices dropped almost 5% to $46.60 as traders worried about an uptick in U.S. drilling activity.</p>
        <p>A similar price rally last year had quickly fizzled. Britain's vote to leave the European Union adds another level of uncertainty, with the effect on markets, oil demand and investment still to be determined.</p>
      </div>
      <footer class="page-foot">August, 2016 | <b>Quarterly News Letter</b><span class="page-num">5</span></footer>
    </article>
  </div>

  <div class="spec" style="top:950px"><span style="left:0">CEO&nbsp; Page</span><span style="left:142px">-</span><span style="left:172px">Single Column + Image Style</span></div>
  <div class="spec" style="top:990px"><span style="left:0">Finance Page</span><span style="left:142px">-</span><span style="left:172px">Top Image + 2 Column + Continuation Page</span></div>
  <div class="spec" style="top:1030px"><span style="left:0">Operations Page</span><span style="left:148px">-</span><span style="left:172px">Top Image + 3 Column Style</span></div>
</div>
</body>
</html>
```